French Bistro Needs a Menu Design for Grand Opening.

We need a menu design incorporating our logo as a design element into the design. The menu needs to be front and back in a 8.5 x 11 inch format. The front of the menu should break up the page into categories for Cocktails, Wines by the Glass, Zero Proof Options, and other beverages.
The back of the menu should break up the page into categories for Appetizers, Charcuterie, Soups and Salads and Entrees.

Here are a few examples of some of the design elements we are interested in. The menu can be either portrait or landscape format.
Thanks,
Calvin

file:///C:/Users/Tomsv/Downloads/Brisol%20Menu.webp

https://img.picvaultexample.net/set/ref-menu-sample-01.jpg

https://img.picvaultexample.net/set/ref-menu-sample-02.jpg

```html
<!DOCTYPE html>
<html lang="en">
<head>
<meta charset="utf-8">
<title>Maison Verel — Menu</title>
<link href="https://fonts.googleapis.com/css2?family=Abril+Fatface&family=Cinzel:wght@700&family=Jost:wght@400&display=swap" rel="stylesheet">
<style>
:root{
  --backdrop:#b3b3b3;
  --paper:#ffffff;
  --ink:#111111;
  --ornament:#dcdcdc;
}
*{margin:0;padding:0;box-sizing:border-box}
html,body{width:919px;height:1200px;overflow:hidden}
body{background:var(--backdrop);position:relative;color:var(--ink)}
.sheet{position:absolute;left:129px;width:660px;height:510px;background:var(--paper)}
.sheet--front{top:76px}
.sheet--back{top:614px}
.frame{position:absolute;left:20px;top:20px;width:621px;height:472px;border:2.5px solid var(--ink)}
.rule-h{position:absolute;left:109px;width:443px;height:0;border-top:1px solid var(--ink)}
.rule-h--top{top:32px}
.rule-h--bottom{top:480px}
.rule-v{position:absolute;width:0;border-left:1px solid var(--ink)}
.ornament{position:absolute;background:var(--ornament)}
.ornament--h{width:72px;height:12px}
.ornament--v{width:12px;height:72px}
.col{position:absolute;width:124px}
.col-1{left:55px}.col-2{left:198px}.col-3{left:343px}.col-4{left:485px}
.section-title{position:absolute;width:150px;text-align:center;font-family:"Abril Fatface",serif;font-size:12.5px;line-height:13.5px;text-transform:uppercase;letter-spacing:.2px}
.item{height:36.3px}
.item-head{display:flex;justify-content:space-between;width:117px;font-family:"Cinzel",serif;font-weight:700;font-size:7.2px;line-height:9px;letter-spacing:.2px;text-transform:uppercase}
.item-desc{font-family:"Jost",sans-serif;font-size:6.2px;line-height:8.6px;white-space:nowrap}
.brand{position:absolute;left:230px;width:200px;text-align:center;font-family:"Cinzel",serif;font-weight:700;color:var(--ink);text-transform:uppercase}
.brand-top{display:block;font-size:16px;letter-spacing:2px;line-height:18px}
.brand-main{display:block;font-size:36px;line-height:38px;letter-spacing:1px}
</style>
</head>
<body>

<section class="sheet sheet--front" aria-label="Drinks menu">
  <div class="frame"></div>
  <div class="rule-h rule-h--top"></div>
  <div class="rule-h rule-h--bottom"></div>
  <div class="ornament ornament--h" style="left:28px;top:27px" role="img" aria-label="Scrollwork corner ornament"></div>
  <div class="ornament ornament--v" style="left:28px;top:27px" role="img" aria-label="Scrollwork corner ornament"></div>
  <div class="ornament ornament--h" style="left:560px;top:27px" role="img" aria-label="Scrollwork corner ornament"></div>
  <div class="ornament ornament--v" style="left:620px;top:27px" role="img" aria-label="Scrollwork corner ornament"></div>
  <div class="ornament ornament--h" style="left:28px;top:472px" role="img" aria-label="Scrollwork corner ornament"></div>
  <div class="ornament ornament--v" style="left:28px;top:412px" role="img" aria-label="Scrollwork corner ornament"></div>
  <div class="ornament ornament--h" style="left:560px;top:472px" role="img" aria-label="Scrollwork corner ornament"></div>
  <div class="ornament ornament--v" style="left:620px;top:412px" role="img" aria-label="Scrollwork corner ornament"></div>
  <div class="rule-v" style="left:32px;top:105px;height:301px"></div>
  <div class="rule-v" style="left:627px;top:105px;height:301px"></div>
  <div class="rule-v" style="left:187px;top:100px;height:352px"></div>
  <div class="rule-v" style="left:330px;top:200px;height:225px"></div>
  <div class="rule-v" style="left:473px;top:100px;height:352px"></div>

  <div class="brand" style="top:52px"><span class="brand-top">Maison</span><span class="brand-main">Verel</span></div>

  <h2 class="section-title" style="left:43px;top:73px">Cocktails</h2>
  <h2 class="section-title" style="left:183px;top:168px">Wines<br>by the glass</h2>
  <h2 class="section-title" style="left:331px;top:169px">Zero proof<br>options</h2>
  <h2 class="section-title" style="left:473px;top:58px">Other<br>beverages</h2>

  <div class="col col-1" style="top:96px">
    <div class="item"><p class="item-head"><span>French 75</span><span>15</span></p><p class="item-desc">When bppers ofuerees, enange rovern,<br>chapring fae epecarts Phenen mcher</p></div>
    <div class="item"><p class="item-head"><span>French 75</span><span>15</span></p><p class="item-desc">When bppers ofuerees, enange rovern,<br>chapring fae epecarts Phenen mcher</p></div>
    <div class="item"><p class="item-head"><span>French 75</span><span>15</span></p><p class="item-desc">When bppers ofuerees, enange rovern,<br>chapring fae epecarts Phenen mcher</p></div>
    <div class="item"><p class="item-head"><span>French 75</span><span>15</span></p><p class="item-desc">When bppers ofuerees, enange rovern,<br>chapring fae epecarts Phenen mcher</p></div>
    <div class="item"><p class="item-head"><span>French 75</span><span>15</span></p><p class="item-desc">When bppers ofuerees, enange rovern,<br>chapring fae epecarts Phenen mcher</p></div>
    <div class="item"><p class="item-head"><span>French 75</span><span>15</span></p><p class="item-desc">When bppers ofuerees, enange rovern,<br>chapring fae epecarts Phenen mcher</p></div>
    <div class="item"><p class="item-head"><span>French 75</span><span>15</span></p><p class="item-desc">When bppers ofuerees, enange rovern,<br>chapring fae epecarts Phenen mcher</p></div>
    <div class="item"><p class="item-head"><span>French 75</span><span>15</span></p><p class="item-desc">When bppers ofuerees, enange rovern,<br>chapring fae epecarts Phenen mcher</p></div>
    <div class="item"><p class="item-head"><span>French 75</span><span>15</span></p><p class="item-desc">When bppers ofuerees, enange rovern,<br>chapring fae epecarts Phenen mcher</p></div>
    <div class="item"><p class="item-head"><span>French 75</span><span>15</span></p><p class="item-desc">When bppers ofuerees, enange rovern,<br>chapring fae epecarts Phenen mcher</p></div>
  </div>
  <div class="col col-2" style="top:205px">
    <div class="item"><p class="item-head"><span>French 75</span><span>15</span></p><p class="item-desc">When bppers ofuerees, enange rovern,<br>chapring fae epecarts Phenen mcher</p></div>
    <div class="item"><p class="item-head"><span>French 75</span><span>15</span></p><p class="item-desc">When bppers ofuerees, enange rovern,<br>chapring fae epecarts Phenen mcher</p></div>
    <div class="item"><p class="item-head"><span>French 75</span><span>15</span></p><p class="item-desc">When bppers ofuerees, enange rovern,<br>chapring fae epecarts Phenen mcher</p></div>
    <div class="item"><p class="item-head"><span>French 75</span><span>15</span></p><p class="item-desc">When bppers ofuerees, enange rovern,<br>chapring fae epecarts Phenen mcher</p></div>
    <div class="item"><p class="item-head"><span>French 75</span><span>15</span></p><p class="item-desc">When bppers ofuerees, enange rovern,<br>chapring fae epecarts Phenen mcher</p></div>
    <div class="item"><p class="item-head"><span>French 75</span><span>15</span></p><p class="item-desc">When bppers ofuerees, enange rovern,<br>chapring fae epecarts Phenen mcher</p></div>
    <div class="item"><p class="item-head"><span>French 75</span><span>15</span></p><p class="item-desc">When bppers ofuerees, enange rovern,<br>chapring fae epecarts Phenen mcher</p></div>
  </div>
  <div class="col col-3" style="top:205px">
    <div class="item"><p class="item-head"><span>French 75</span><span>15</span></p><p class="item-desc">When bppers ofuerees, enange rovern,<br>chapring fae epecarts Phenen mcher</p></div>
    <div class="item"><p class="item-head"><span>French 75</span><span>15</span></p><p class="item-desc">When bppers ofuerees, enange rovern,<br>chapring fae epecarts Phenen mcher</p></div>
    <div class="item"><p class="item-head"><span>French 75</span><span>15</span></p><p class="item-desc">When bppers ofuerees, enange rovern,<br>chapring fae epecarts Phenen mcher</p></div>
    <div class="item"><p class="item-head"><span>French 75</span><span>15</span></p><p class="item-desc">When bppers ofuerees, enange rovern,<br>chapring fae epecarts Phenen mcher</p></div>
    <div class="item"><p class="item-head"><span>French 75</span><span>15</span></p><p class="item-desc">When bppers ofuerees, enange rovern,<br>chapring fae epecarts Phenen mcher</p></div>
    <div class="item"><p class="item-head"><span>French 75</span><span>15</span></p><p class="item-desc">When bppers ofuerees, enange rovern,<br>chapring fae epecarts Phenen mcher</p></div>
    <div class="item"><p class="item-head"><span>French 75</span><span>15</span></p><p class="item-desc">When bppers ofuerees, enange rovern,<br>chapring fae epecarts Phenen mcher</p></div>
  </div>
  <div class="col col-4" style="top:96px">
    <div class="item"><p class="item-head"><span>French 75</span><span>15</span></p><p class="item-desc">When bppers ofuerees, enange rovern,<br>chapring fae epecarts Phenen mcher</p></div>
    <div class="item"><p class="item-head"><span>French 75</span><span>15</span></p><p class="item-desc">When bppers ofuerees, enange rovern,<br>chapring fae epecarts Phenen mcher</p></div>
    <div class="item"><p class="item-head"><span>French 75</span><span>15</span></p><p class="item-desc">When bppers ofuerees, enange rovern,<br>chapring fae epecarts Phenen mcher</p></div>
    <div class="item"><p class="item-head"><span>French 75</span><span>15</span></p><p class="item-desc">When bppers ofuerees, enange rovern,<br>chapring fae epecarts Phenen mcher</p></div>
    <div class="item"><p class="item-head"><span>French 75</span><span>15</span></p><p class="item-desc">When bppers ofuerees, enange rovern,<br>chapring fae epecarts Phenen mcher</p></div>
    <div class="item"><p class="item-head"><span>French 75</span><span>15</span></p><p class="item-desc">When bppers ofuerees, enange rovern,<br>chapring fae epecarts Phenen mcher</p></div>
    <div class="item"><p class="item-head"><span>French 75</span><span>15</span></p><p class="item-desc">When bppers ofuerees, enange rovern,<br>chapring fae epecarts Phenen mcher</p></div>
    <div class="item"><p class="item-head"><span>French 75</span><span>15</span></p><p class="item-desc">When bppers ofuerees, enange rovern,<br>chapring fae epecarts Phenen mcher</p></div>
    <div class="item"><p class="item-head"><span>French 75</span><span>15</span></p><p class="item-desc">When bppers ofuerees, enange rovern,<br>chapring fae epecarts Phenen mcher</p></div>
    <div class="item"><p class="item-head"><span>French 75</span><span>15</span></p><p class="item-desc">When bppers ofuerees, enange rovern,<br>chapring fae epecarts Phenen mcher</p></div>
  </div>
</section>

<section class="sheet sheet--back" aria-label="Food menu">
  <div class="frame"></div>
  <div class="rule-h rule-h--top"></div>
  <div class="rule-h rule-h--bottom"></div>
  <div class="ornament ornament--h" style="left:28px;top:27px" role="img" aria-label="Scrollwork corner ornament"></div>
  <div class="ornament ornament--v" style="left:28px;top:27px" role="img" aria-label="Scrollwork corner ornament"></div>
  <div class="ornament ornament--h" style="left:560px;top:27px" role="img" aria-label="Scrollwork corner ornament"></div>
  <div class="ornament ornament--v" style="left:620px;top:27px" role="img" aria-label="Scrollwork corner ornament"></div>
  <div class="ornament ornament--h" style="left:28px;top:472px" role="img" aria-label="Scrollwork corner ornament"></div>
  <div class="ornament ornament--v" style="left:28px;top:412px" role="img" aria-label="Scrollwork corner ornament"></div>
  <div class="ornament ornament--h" style="left:560px;top:472px" role="img" aria-label="Scrollwork corner ornament"></div>
  <div class="ornament ornament--v" style="left:620px;top:412px" role="img" aria-label="Scrollwork corner ornament"></div>
  <div class="rule-v" style="left:32px;top:111px;height:304px"></div>
  <div class="rule-v" style="left:627px;top:111px;height:304px"></div>
  <div class="rule-v" style="left:187px;top:114px;height:329px"></div>
  <div class="rule-v" style="left:330px;top:109px;height:219px"></div>
  <div class="rule-v" style="left:473px;top:103px;height:340px"></div>

  <h2 class="section-title" style="left:43px;top:74px">Appetizers</h2>
  <h2 class="section-title" style="left:183px;top:74px">Charcuterie</h2>
  <h2 class="section-title" style="left:331px;top:70px">Soups and<br>salads</h2>
  <h2 class="section-title" style="left:473px;top:69px">Entrees</h2>

  <div class="brand" style="top:371px"><span class="brand-top">Maison</span><span class="brand-main">Verel</span></div>

  <div class="col col-1" style="top:96px">
    <div class="item"><p class="item-head"><span>French 75</span><span>15</span></p><p class="item-desc">When bppers ofuerees, enange rovern,<br>chapring fae epecarts Phenen mcher</p></div>
    <div class="item"><p class="item-head"><span>French 75</span><span>15</span></p><p class="item-desc">When bppers ofuerees, enange rovern,<br>chapring fae epecarts Phenen mcher</p></div>
    <div class="item"><p class="item-head"><span>French 75</span><span>15</span></p><p class="item-desc">When bppers ofuerees, enange rovern,<br>chapring fae epecarts Phenen mcher</p></div>
    <div class="item"><p class="item-head"><span>French 75</span><span>15</span></p><p class="item-desc">When bppers ofuerees, enange rovern,<br>chapring fae epecarts Phenen mcher</p></div>
    <div class="item"><p class="item-head"><span>French 75</span><span>15</span></p><p class="item-desc">When bppers ofuerees, enange rovern,<br>chapring fae epecarts Phenen mcher</p></div>
    <div class="item"><p class="item-head"><span>French 75</span><span>15</span></p><p class="item-desc">When bppers ofuerees, enange rovern,<br>chapring fae epecarts Phenen mcher</p></div>
    <div class="item"><p class="item-head"><span>French 75</span><span>15</span></p><p class="item-desc">When bppers ofuerees, enange rovern,<br>chapring fae epecarts Phenen mcher</p></div>
    <div class="item"><p class="item-head"><span>French 75</span><span>15</span></p><p class="item-desc">When bppers ofuerees, enange rovern,<br>chapring fae epecarts Phenen mcher</p></div>
    <div class="item"><p class="item-head"><span>French 75</span><span>15</span></p><p class="item-desc">When bppers ofuerees, enange rovern,<br>chapring fae epecarts Phenen mcher</p></div>
    <div class="item"><p class="item-head"><span>French 75</span><span>15</span></p><p class="item-desc">When bppers ofuerees, enange rovern,<br>chapring fae epecarts Phenen mcher</p></div>
  </div>
  <div class="col col-2" style="top:105px">
    <div class="item"><p class="item-head"><span>French 75</span><span>15</span></p><p class="item-desc">When bppers ofuerees, enange rovern,<br>chapring fae epecarts Phenen mcher</p></div>
    <div class="item"><p class="item-head"><span>French 75</span><span>15</span></p><p class="item-desc">When bppers ofuerees, enange rovern,<br>chapring fae epecarts Phenen mcher</p></div>
    <div class="item"><p class="item-head"><span>French 75</span><span>15</span></p><p class="item-desc">When bppers ofuerees, enange rovern,<br>chapring fae epecarts Phenen mcher</p></div>
    <div class="item"><p class="item-head"><span>French 75</span><span>15</span></p><p class="item-desc">When bppers ofuerees, enange rovern,<br>chapring fae epecarts Phenen mcher</p></div>
    <div class="item"><p class="item-head"><span>French 75</span><span>15</span></p><p class="item-desc">When bppers ofuerees, enange rovern,<br>chapring fae epecarts Phenen mcher</p></div>
    <div class="item"><p class="item-head"><span>French 75</span><span>15</span></p><p class="item-desc">When bppers ofuerees, enange rovern,<br>chapring fae epecarts Phenen mcher</p></div>
    <div class="item"><p class="item-head"><span>French 75</span><span>15</span></p><p class="item-desc">When bppers ofuerees, enange rovern,<br>chapring fae epecarts Phenen mcher</p></div>
  </div>
  <div class="col col-3" style="top:105px">
    <div class="item"><p class="item-head"><span>French 75</span><span>15</span></p><p class="item-desc">When bppers ofuerees, enange rovern,<br>chapring fae epecarts Phenen mcher</p></div>
    <div class="item"><p class="item-head"><span>French 75</span><span>15</span></p><p class="item-desc">When bppers ofuerees, enange rovern,<br>chapring fae epecarts Phenen mcher</p></div>
    <div class="item"><p class="item-head"><span>French 75</span><span>15</span></p><p class="item-desc">When bppers ofuerees, enange rovern,<br>chapring fae epecarts Phenen mcher</p></div>
    <div class="item"><p class="item-head"><span>French 75</span><span>15</span></p><p class="item-desc">When bppers ofuerees, enange rovern,<br>chapring fae epecarts Phenen mcher</p></div>
    <div class="item"><p class="item-head"><span>French 75</span><span>15</span></p><p class="item-desc">When bppers ofuerees, enange rovern,<br>chapring fae epecarts Phenen mcher</p></div>
    <div class="item"><p class="item-head"><span>French 75</span><span>15</span></p><p class="item-desc">When bppers ofuerees, enange rovern,<br>chapring fae epecarts Phenen mcher</p></div>
    <div class="item"><p class="item-head"><span>French 75</span><span>15</span></p><p class="item-desc">When bppers ofuerees, enange rovern,<br>chapring fae epecarts Phenen mcher</p></div>
  </div>
  <div class="col col-4" style="top:96px">
    <div class="item"><p class="item-head"><span>French 75</span><span>15</span></p><p class="item-desc">When bppers ofuerees, enange rovern,<br>chapring fae epecarts Phenen mcher</p></div>
    <div class="item"><p class="item-head"><span>French 75</span><span>15</span></p><p class="item-desc">When bppers ofuerees, enange rovern,<br>chapring fae epecarts Phenen mcher</p></div>
    <div class="item"><p class="item-head"><span>French 75</span><span>15</span></p><p class="item-desc">When bppers ofuerees, enange rovern,<br>chapring fae epecarts Phenen mcher</p></div>
    <div class="item"><p class="item-head"><span>French 75</span><span>15</span></p><p class="item-desc">When bppers ofuerees, enange rovern,<br>chapring fae epecarts Phenen mcher</p></div>
    <div class="item"><p class="item-head"><span>French 75</span><span>15</span></p><p class="item-desc">When bppers ofuerees, enange rovern,<br>chapring fae epecarts Phenen mcher</p></div>
    <div class="item"><p class="item-head"><span>French 75</span><span>15</span></p><p class="item-desc">When bppers ofuerees, enange rovern,<br>chapring fae epecarts Phenen mcher</p></div>
    <div class="item"><p class="item-head"><span>French 75</span><span>15</span></p><p class="item-desc">When bppers ofuerees, enange rovern,<br>chapring fae epecarts Phenen mcher</p></div>
    <div class="item"><p class="item-head"><span>French 75</span><span>15</span></p><p class="item-desc">When bppers ofuerees, enange rovern,<br>chapring fae epecarts Phenen mcher</p></div>
    <div class="item"><p class="item-head"><span>French 75</span><span>15</span></p><p class="item-desc">When bppers ofuerees, enange rovern,<br>chapring fae epecarts Phenen mcher</p></div>
    <div class="item"><p class="item-head"><span>French 75</span><span>15</span></p><p class="item-desc">When bppers ofuerees, enange rovern,<br>chapring fae epecarts Phenen mcher</p></div>
  </div>
</section>

</body>
</html>
```